Seeds of Renewal needs a business card design

I need a business card design for my company to promote my new Christian non-fiction book, "Where the Quiet River Bends." I also want it to promote my web site, www.seedsofrenewalway.com. The book is about empowering people to be transformed through a deeper relationship with God. I am picturing a design with a dove over water that matches the colors of my book cover, blue, white, yellow, and orange. Fire and light would also be possible elements of the design. I would like to be able to use the dove by itself as a logo for my business. This is my first book and I do not know if others will follow. The name of my publishing company is Lantern Valley Press, named after Gideon in the Bible story from the book of Judges. My book was independently published and was recently selected as a finalist for the 2015 Bright Horizon SMALLPRESS book prize in the Christian non-fiction genre.

Target Market(s)

People who are hungry for more of God and who want to experience deep change in their lives.

Industry/Entity Type

Business

Contact Information for Business Card

Dana Whitfield
Author
Where the Quiet River Bends
4283 Maple Hollow Lane
Austin, Texas 78952-1184
512-555-0147 512-555-0193
dana-whitfield@brightmailbox.net
www.seedsofrenewalway.com

Colors
0355a3
3377b5
85acd3
cedeed
fbee3e
ffc214

Requirements
Must have
• A dove with a blue background, peaceful and appealing
Nice to have
• Water and fire or light
Should not have
• Violence or fear-producing images

```html
<!DOCTYPE html>
<html lang="en">
<head>
<meta charset="utf-8">
<title>Dana Whitfield — Business Card</title>
<link rel="stylesheet" href="https://fonts.googleapis.com/css2?family=Fira+Sans:wght@300;400;700;800&display=swap">
<style>
  :root {
    --deep-navy: #1b1f6e;
    --ocean-blue: #0355a3;
    --sea-blue: #1a7fc0;
    --sky-cyan: #38b6e6;
    --glow-cyan: #a6e8f2;
    --light-glow: #e6fbff;
    --name-gold: #ffb81c;
    --text-white: #ffffff;
  }
  html, body {
    margin: 0;
    padding: 0;
    width: 1200px;
    height: 734px;
    overflow: hidden;
    background: #ffffff;
  }
  .card {
    position: relative;
    width: 1200px;
    height: 734px;
    overflow: hidden;
    font-family: "Fira Sans", sans-serif;
    color: var(--text-white);
  }
  .sea-and-light {
    position: absolute;
    inset: 0;
    background:
      radial-gradient(ellipse 420px 360px at 230px 170px, var(--light-glow) 0%, var(--glow-cyan) 18%, rgba(56,182,230,0.55) 45%, rgba(56,182,230,0) 75%),
      linear-gradient(180deg, var(--sky-cyan) 0%, var(--sea-blue) 32%, var(--ocean-blue) 58%, #1d3f9a 78%, var(--deep-navy) 100%);
  }
  .dove-artwork {
    position: absolute;
    left: 45px;
    top: 40px;
    width: 452px;
    height: 355px;
    border-radius: 50%;
    background: radial-gradient(ellipse at 45% 45%, rgba(255,255,255,0.85) 0%, rgba(255,255,255,0.35) 45%, rgba(255,255,255,0) 72%);
  }
  .author-block {
    position: absolute;
    left: 628px;
    top: 288px;
  }
  .author-name {
    margin: 0;
    font-weight: 800;
    font-size: 46px;
    line-height: 1;
    letter-spacing: 1px;
    color: var(--name-gold);
    text-transform: uppercase;
  }
  .author-role {
    margin: 6px 0 0;
    font-weight: 300;
    font-size: 50px;
    line-height: 1;
    color: var(--text-white);
  }
  .contact {
    position: absolute;
    left: 68px;
    top: 462px;
    margin: 0;
    font-style: normal;
  }
  .contact-line {
    display: block;
    white-space: nowrap;
  }
  .contact-line--large {
    font-weight: 400;
    font-size: 39px;
    line-height: 56px;
  }
  .contact-line--email {
    font-weight: 400;
    font-size: 34px;
    line-height: 55px;
  }
  .contact-line--web {
    font-weight: 700;
    font-size: 34px;
    line-height: 56px;
  }
</style>
</head>
<body>
  <main class="card">
    <div class="sea-and-light" role="img" aria-label="Rippling blue water beneath bright rays of light"></div>
    <div class="dove-artwork" role="img" aria-label="White dove in flight within a burst of light"></div>

    <div class="author-block">
      <h1 class="author-name">Dana Whitfield</h1>
      <p class="author-role">autor</p>
    </div>

    <address class="contact">
      <span class="contact-line contact-line--large">4283 Maple Hollow Lane | Austin | Texas</span>
      <span class="contact-line contact-line--large">78952-1184 512-555-0147 512-555-0193</span>
      <span class="contact-line contact-line--email">dana-whitfield@brightmailbox</span>
      <span class="contact-line contact-line--web">net www.seedsofrenewalway.com</span>
    </address>
  </main>
</body>
</html>
```